New look and feel for investment website

Hi

Our website needs a crisp and professional look and feel applying to it. Here’s the address: http://www.brightplinth.co.uk. Since posting the brief yesterday (Tuesday, 16 August), we've reduced the amount of content on the home page, which should make life a little easier for you. We will come back later today, with some points of reference in terms of sites we like the look of. (See below)

17 August, 1.20pm GMT. OK, comments generally on the designs submitted so far. Please keep in mind that images of graphs, piles of coins, paper money and pretty females are not what is required. Better to think in terms of abstract imagery instead. Ratios? Circles? Relationships? Patterns? Not money,sex,graphs etc. Hope that helps.

For guidance on look and feel, please refer to these sites, which we like:

http://www.morvelle.co.uk/
http://www.qz.com/
https://www.harrowfieldtamsin.com
https://www.pirelconcerns.com
https://www.kvantule.com
Updates

Here's the Tall Beacons logo created in AI CS5.

Our market is professional financial advisers and relatively sophisticated private investors. The look and feel therefore should be slick and sophisticated - not 'lively' and lightweight, more like a banking site. Please read the brief again where we've added a list of websites that we really like the look of to get a better feel for what we're looking for. Thanks once again, we appreciate the work you're putting in.

It's essential that all the elements that are on the current home page be included on all new designs. 

We use a device in our e-mails which you may wish to incorporate in your design.

Target Market(s)

Professional financial advisers. People who know about investment and money.

Industry/Entity Type

Investment

Requirements
Should not have
• Graphs or people.

```html
<!DOCTYPE html>
<html lang="en">
<head>
<meta charset="utf-8">
<title>Tall Beacons – Home</title>
<link href="https://fonts.googleapis.com/css2?family=Noto+Sans:wght@400;600;700&display=swap" rel="stylesheet">
<style>
:root{
  --maroon:#9b0b34;
  --page:#e4e4e4;
  --white:#ffffff;
  --ink:#2b2b2b;
  --brand-ink:#5e5e5e;
  --panel:#e9e9e9;
  --panel-line:#c9c9c9;
  --orange:#f0962e;
  --hero-dark:#b9b9bb;
  --icon:#9a9a9a;
}
*{box-sizing:border-box;margin:0;padding:0}
html,body{width:1080px;height:1200px;overflow:hidden}
body{background:var(--page);font-family:"Noto Sans",Verdana,sans-serif;color:var(--ink);position:relative}
.sheet{position:absolute;left:55px;top:0;width:991px;height:1200px;background:var(--white)}
.top-band{position:absolute;left:55px;top:0;width:991px;height:40px;background:var(--maroon);border-radius:0 0 4px 4px}
.top-dot{position:absolute;left:55px;top:14px;width:54px;height:54px;border-radius:50%;background:var(--maroon)}
.brand{position:absolute;left:147px;top:58px;font-size:44px;font-weight:600;color:var(--brand-ink);letter-spacing:-0.5px;line-height:1}
.top-nav{position:absolute;right:58px;top:88px;font-size:14px;color:#555;display:flex;gap:12px}
.top-nav .sep{color:#999}
.hero{position:absolute;left:55px;top:126px;width:991px;height:177px;overflow:hidden}
.hero-photo{position:absolute;right:0;top:0;width:520px;height:177px;background:linear-gradient(90deg,#ffffff 0%,#e8e8ea 35%,var(--hero-dark) 75%,#8e8e92 100%);border-radius:0 6px 0 0}
.hero-text{position:absolute;left:62px;top:40px;font-size:15.5px;line-height:21px;color:#111;width:560px}
.hero-offer{position:absolute;left:62px;top:126px;font-size:30px;font-weight:700;color:var(--maroon)}
.content{position:absolute;left:55px;top:330px;width:630px}
.tab{height:32px;width:245px;background:var(--maroon);color:#fff;font-size:13px;font-weight:600;line-height:32px;padding:0 22px 0 20px;border-radius:0 16px 16px 0;white-space:nowrap}
.copy{font-size:13px;line-height:18px;color:#333;margin:10px 0 0 60px;width:560px}
.gap1{margin-top:20px}
.links{position:absolute;left:115px;top:938px;font-size:13px;line-height:19px;color:#222}
.links .arr{color:var(--orange);font-weight:700;margin-left:14px;font-size:11px}
.note{position:absolute;left:115px;top:985px;width:520px;font-size:9.5px;line-height:12.5px;color:var(--orange)}
.social{position:absolute;left:115px;top:1068px;display:flex;gap:6px}
.social span{width:20px;height:20px;border-radius:3px;background:var(--icon)}
.footer-rule{position:absolute;left:250px;top:1101px;width:560px;height:2px;background:linear-gradient(90deg,transparent,#bbb,transparent)}
.footer{position:absolute;left:145px;top:1128px;width:800px;font-size:10.3px;line-height:13.5px;color:#444;text-align:center}
.panel{position:absolute;left:700px;width:346px;background:var(--panel);border:1px solid #d6d6d6;border-radius:8px}
.notch{position:absolute;left:-20px;width:40px;height:40px;border-radius:50%;background:var(--white)}
.side-nav{top:324px;height:218px;padding:8px 0 0 24px;font-size:13.4px;line-height:18.5px;color:#222;list-style:none}
.reg{top:553px;height:177px;padding:14px 20px 0 24px}
.reg h2{font-size:19px;font-weight:700;color:var(--orange);text-align:center;margin-bottom:10px}
.reg p{font-size:11.6px;line-height:16px;color:#333}
.reg-cta{margin-top:10px;border:1px solid #f2c99a;background:#fff;padding:4px 8px;font-size:11.6px;line-height:15px;color:var(--orange)}
.stats{top:742px;height:333px;padding:8px 24px 0 24px;font-size:11.6px;line-height:15.5px;color:#444}
.stats p{border-bottom:1px solid var(--panel-line);padding:4px 0 5px}
.stats p:last-child{border-bottom:none}
</style>
</head>
<body>
<div class="sheet"></div>
<div class="top-dot"></div>
<div class="top-band"></div>

<header>
  <div class="brand">Tall Beacons</div>
  <nav class="top-nav"><span>Login</span><span class="sep">|</span><span>Register for free</span><span class="sep">|</span><span>Contact us</span><span class="sep">|</span><span>Terms &amp; Conditions</span></nav>
</header>

<section class="hero">
  <div class="hero-photo" role="img" aria-label="Photograph of a keyboard with a bank card resting on it"></div>
  <p class="hero-text">A potential return of 23.57 % a year<br>from America's biggest businesses with the emphasis firmly<br>on capital preservation. (OK: we know you've yet to learn to love it,<br>so that's why you can use our service</p>
  <p class="hero-offer">free of charge or six months!)</p>
</section>

<main class="content">
  <div class="tab">Something different...</div>
  <p class="copy">You may well be thinking that Tall Beacons is just another one of those banal share recommendation sites sprinkled with the usual idiotic and patronising platitudes, gross exaggerations, silly get-rich-quick promises and all the other stuff and nonsense you associate with the black art of share-tipping...<br>Well, we have a pleasant surprise for you: you couldn't be further from the truth.</p>

  <div class="tab gap1">No! No! No!</div>
  <p class="copy">There's no newsletter to read, books to study, dvds to watch or traders' secrets to be revealed. No neverending stream of recommendations. No webcasts. No effort or time to invest. No training. No research. No tedious market commentaries. And no financial discomfort for you whatsoever. (At least for the first six months that is!)</p>

  <div class="tab gap1">Undervalued and overlooked</div>
  <p class="copy">Our program finds stocks that appear to be undervalued - i.e., where the price of a company's share does no reflect the real worth of the business. We confine our search to 1,000 of the USA's biggest companies; successful, robust, large cap businesses, which for one reason or another are either unpopular with investors or overlooked by them</p>

  <div class="tab gap1">We don't get it right every time...</div>
  <p class="copy">We do however, get it right 75.58 % of the time (the total of all our winning trades out of all our trades) and on that basis tracking our portfolio should produce an average return of 23.57 % a year for you.<br>An average of five trades a year and never more than five holdings. We tested different numbers of holdings and capital allocation percentages. The best results came from a portfolio of no more than five holdings with the same amount of capital allocated to each holding. That's it. You don't have to do it that way, but it works for us.</p>
</main>

<div class="links">
  <p>For a succinct explanation of our service and the results to date...please go here<span class="arr">&#9654;&#9654;</span></p>
  <p>More about the strategy we use to choose stocks...<span class="arr">&#9654;&#9654;</span></p>
</div>
<p class="note">If you have any questions, please e-mail info@tallbeacons.co.uk. Although we're very willing to answer queries about the way we pick stocks, please do keep in mind that as we're giving this service away free of charge initially, we're not inclined to expend time and energy debating the relative merits of value investing or fundamental analyses. Other than that, fire away!</p>

<div class="social" aria-label="Social links">
  <span></span><span></span><span></span><span></span><span></span>
</div>

<ul class="panel side-nav">
  <li>Home</li><li>Two Minute Guide</li><li>Current &amp; year to date performance</li><li>Watch list</li><li>Other key numbers</li><li>Back tested results</li><li>History of all trades</li><li>FAQs</li><li>About our analyses</li><li>About value investing</li><li>The Meridian 1000 and the Halden 500 index</li>
  <span class="notch" style="top:70px"></span>
</ul>

<aside class="panel reg">
  <span class="notch" style="top:60px"></span>
  <h2>FREE REGISTRATION</h2>
  <p>We're not asking you to part company with any money —at least not right now. All we need from you at the moment is your e-mail address then you'll be able to view our portfolio and Watch list for 6 months free of charge!</p>
  <div class="reg-cta">To use our service free of charge for six months, please go here...</div>
</aside>

<aside class="panel stats">
  <span class="notch" style="top:150px"></span>
  <p>Average, annualised compound return over to:<br>23.57 %</p>
  <p>So far this year, the portfolio's return is 13.49 %:</p>
  <p>Worst ever annual loss: -1.48 %;<br>best ever annual gain: 69.77 %</p>
  <p>Average return per trade including losing trades: 24.44 %</p>
  <p>Maximum number of winning/losing trades in a row: 11/4.</p>
  <p>Average number of days a stock stays in the portfolio: 287</p>
  <p>An average of five trades a year and never more than five holdings at any one time.</p>
  <p>86 trades in total, of which 65 were profitable - a success rate of 75.58 %</p>
</aside>

<div class="footer-rule"></div>
<footer class="footer">This website is published by Tall Beacons Ltd. Registered in England No. 08136529. Registered office: 48 Corbel Lane London N7 2QT. This website and its content is the copyright of Tall Beacons Ltd - © Tall Beacons Ltd 2011. All rights reserved. Any redistribution or reproduction of part or all of the contents in any form is prohibited other than the following: you may print or download to a local hard disk extracts for your personal and non-commercial use only you may copy the content to individual third parties for their personal use, but</footer>
</body>
</html>
```